Highly rated moving company needs postcard design

We need a highly converting postcard to send when people put their homes for sale online. This should highlight the fact that we're Austin's highest rated moving company, and should convey quality and value. We do local, statewide and long distance moves. We also do office and commerical moves and storage. final design must be sized to work with our mailing system. Please see attached file for more information.

```html
<!DOCTYPE html>
<html lang="en">
<head>
<meta charset="utf-8">
<title>Hilltop Haulers Postcard</title>
<link rel="stylesheet" href="https://fonts.googleapis.com/css2?family=Cabin:wght@400;500;700&family=Roboto:ital,wght@1,300;1,900&display=swap">
<style>
:root{
  --navy:#24206b;
  --red:#e6202a;
  --white:#ffffff;
  --page:#c6c6c6;
  --ink:#2a2a3a;
  --orange:#e8711c;
  --green:#34a853;
}
*{box-sizing:border-box;margin:0;padding:0}
html,body{width:1000px;height:1200px;overflow:hidden;background:var(--page)}
body{position:relative;font-family:"Cabin",sans-serif;color:var(--navy)}
.card{position:absolute;left:149px;width:702px;height:469px;background:var(--white);overflow:hidden}
.card--front{top:95px}
.card--back{top:630px}
.abs{position:absolute}
.headline{left:26px;top:20px;font-family:"Roboto",sans-serif;font-style:italic;font-weight:900;font-size:31px;line-height:40px;color:var(--navy)}
.service-tag{left:26px;height:27px;padding:0 6px;background:var(--navy);color:var(--white);font-size:15.5px;line-height:27px;white-space:nowrap}
.brand{display:flex;align-items:center;gap:8px}
.brand__dot{width:34px;height:34px;border-radius:50%;background:var(--navy);flex:none}
.brand__name{font-family:"Cabin",sans-serif;font-weight:700;color:var(--red);line-height:1;letter-spacing:2px}
.website{font-size:12.5px;color:var(--navy)}
.phone{display:flex;align-items:center;gap:10px;font-family:"Roboto",sans-serif;font-style:italic;font-weight:300;letter-spacing:3px;white-space:nowrap}
.ratings-bar{left:208px;top:342px;width:500px;height:69px;background:var(--white);border-radius:14px 0 0 14px;box-shadow:0 2px 6px rgba(0,0,0,.18)}
.rating-block{font-family:"Roboto",sans-serif;font-style:normal}
.rating-block__label{font-size:6px;color:#444;font-family:"Cabin",sans-serif}
.rating-block__score{font-size:9px;color:var(--orange);font-family:"Cabin",sans-serif;letter-spacing:1px}
.rating-block__more{font-size:5.5px;color:#777;font-family:"Cabin",sans-serif}
.badge{position:absolute;border-radius:5px}
.section-title{left:27px;top:20px;font-family:"Roboto",sans-serif;font-style:italic;font-weight:900;font-size:33px;color:var(--navy)}
.feature{position:absolute;top:129px;width:98px;height:133px;border:1px solid var(--navy);border-radius:0 0 5px 5px}
.feature__title{height:19px;background:var(--navy);color:var(--white);font-size:10.5px;line-height:19px;text-align:center;white-space:nowrap}
.feature__text{padding:7px 10px 0 10px;font-size:6.9px;line-height:9.7px;text-align:justify;color:var(--ink)}
.feature-icon{position:absolute;top:78px;width:46px;height:46px;border-radius:50%;background:var(--navy)}
.review-card{left:241px;top:284px;width:97px;height:159px;border:1px solid #b9b9c8;box-shadow:0 1px 4px rgba(0,0,0,.2);padding:8px 10px}
.review-card__quote{margin-top:8px;font-size:8.2px;line-height:11px;text-align:justify;color:var(--ink)}
.review-card__name{margin-top:2px;font-size:8px;color:var(--ink);font-weight:500}
.service-pill{position:absolute;left:584px;width:118px;height:19px;background:var(--red);color:var(--white);border-radius:10px 0 0 10px;border:1.5px solid var(--white);border-right:none;font-size:9.3px;line-height:16px;padding-left:8px;white-space:nowrap}
.tagline{left:397px;top:200px;font-family:"Roboto",sans-serif;font-style:italic;font-weight:900;font-size:22.5px;color:var(--navy);white-space:nowrap}
.tagline em{color:var(--red);font-style:italic}
.phone-bar{left:380px;top:236px;width:322px;height:37px;background:var(--navy);color:var(--white);justify-content:center}
.address-line{position:absolute;left:380px;width:196px;height:1px;background:var(--navy)}
.stamp-box{left:610px;top:314px;width:79px;height:98px;border:1px dashed var(--navy)}
</style>
</head>
<body>

<svg width="0" height="0" style="position:absolute" aria-hidden="true">
  <defs>
    <symbol id="burst" viewBox="-50 -50 100 100">
      <polygon fill="var(--red)" points="48,0 37.7,10.1 41.6,24 27.6,27.6 24,41.6 10.1,37.7 0,48 -10.1,37.7 -24,41.6 -27.6,27.6 -41.6,24 -37.7,10.1 -48,0 -37.7,-10.1 -41.6,-24 -27.6,-27.6 -24,-41.6 -10.1,-37.7 0,-48 10.1,-37.7 24,-41.6 27.6,-27.6 41.6,-24 37.7,-10.1"/>
    </symbol>
    <symbol id="phone-icon" viewBox="0 0 24 24">
      <path fill="currentColor" d="M6.6 10.8a15.1 15.1 0 0 0 6.6 6.6l2.2-2.2a1 1 0 0 1 1-.25 11.4 11.4 0 0 0 3.6.57 1 1 0 0 1 1 1V20a1 1 0 0 1-1 1A17 17 0 0 1 3 4a1 1 0 0 1 1-1h3.5a1 1 0 0 1 1 1c0 1.25.2 2.45.57 3.57a1 1 0 0 1-.25 1z"/>
    </symbol>
    <linearGradient id="photo-front" x1="0" y1="0" x2="1" y2="1">
      <stop offset="0" stop-color="#eeece8"/>
      <stop offset=".55" stop-color="#b39a86"/>
      <stop offset="1" stop-color="#2a3150"/>
    </linearGradient>
    <linearGradient id="photo-back" x1="0" y1="0" x2="0" y2="1">
      <stop offset="0" stop-color="#f3f1ee"/>
      <stop offset=".6" stop-color="#d9c7b2"/>
      <stop offset="1" stop-color="#b99b78"/>
    </linearGradient>
  </defs>
</svg>

<!-- FRONT -->
<section class="card card--front">
  <svg class="abs" style="left:0;top:0" width="702" height="469" viewBox="0 0 702 469">
    <path role="img" aria-label="Photo of a smiling family of three embracing in their new home" fill="url(#photo-front)" d="M330,0 L702,0 L702,469 L476,469 C385,380 338,200 330,0 Z"/>
    <path fill="var(--red)" d="M322,0 L330,0 C338,200 385,380 478,469 L460,469 C372,385 328,200 322,0 Z"/>
  </svg>

  <h1 class="abs headline">Moving Soon?<br>Choose Austin’s<br>Highest Rated<br>Moving Company!</h1>

  <div class="abs service-tag" style="top:190px">Local, Statewide, and Long Distance Moves</div>
  <div class="abs service-tag" style="top:226px">Office and Commercial Moves</div>
  <div class="abs service-tag" style="top:262px">Secure Storage Solutions</div>

  <div class="abs" style="left:243px;top:231px;width:96px;height:96px">
    <svg width="96" height="96"><use href="#burst"/></svg>
    <div class="abs" style="left:0;top:0;width:96px;height:96px;display:flex;align-items:center;justify-content:center;transform:rotate(-35deg);color:var(--white);font-weight:700;font-size:14.5px;line-height:15px;text-align:center;letter-spacing:1px">GET<br>A FREE<br>QUOTE</div>
  </div>

  <div class="abs brand" style="left:26px;top:340px">
    <span class="brand__dot"></span>
    <span class="brand__name" style="font-size:22px">HILLTOP<br>HAULERS</span>
  </div>
  <div class="abs website" style="left:26px;top:430px">www.hilltophaulersatx.com</div>

  <div class="ratings-bar abs">
    <div class="abs" style="left:8px;top:13px;width:97px;height:1.5px;background:var(--green)"></div>
    <div class="abs rating-block" style="left:36px;top:20px">
      <div class="rating-block__label">Customer Rating</div>
      <div class="rating-block__score">5.0 ★★★★★</div>
      <div class="rating-block__more">See all our reviews</div>
    </div>
    <div class="badge" style="left:117px;top:17px;width:91px;height:35px;background:var(--navy)"></div>
    <div class="badge" style="left:221px;top:20px;width:77px;height:30px;background:#2aa4dc;border-radius:14px"></div>
    <div class="badge" style="left:311px;top:22px;width:78px;height:27px;background:var(--red)"></div>
    <div class="badge" style="left:402px;top:16px;width:78px;height:37px;background:#1c1c1c"></div>
  </div>

  <div class="abs phone" style="left:233px;top:425px;font-size:25px;color:var(--navy)">
    <svg width="20" height="20" style="color:var(--navy)"><use href="#phone-icon"/></svg>
    <span>512-555-0148</span>
  </div>
</section>

<!-- BACK -->
<section class="card card--back">
  <h2 class="abs section-title">Why Choose Us?</h2>

  <div class="feature-icon" style="left:55px">
    <svg width="46" height="46" viewBox="0 0 46 46"><circle cx="23" cy="21" r="11" fill="none" stroke="#fff" stroke-width="2.5"/><path d="M18 21l4 4 7-7" fill="none" stroke="#fff" stroke-width="2.5"/><path d="M15 30l-4 7 5-1 2 4 3-7M31 30l4 7-5-1-2 4-3-7" fill="#fff"/></svg>
  </div>
  <div class="feature-icon" style="left:161px">
    <svg width="46" height="46" viewBox="0 0 46 46"><circle cx="23" cy="23" r="13" fill="#fff"/><circle cx="23" cy="23" r="8" fill="none" stroke="var(--navy)" stroke-width="2.5"/><path d="M23 18v5l3 2" fill="none" stroke="var(--navy)" stroke-width="2"/></svg>
  </div>
  <div class="feature-icon" style="left:266px">
    <svg width="46" height="46" viewBox="0 0 46 46"><circle cx="25" cy="17" r="8" fill="#fff"/><text x="25" y="21" text-anchor="middle" font-family="Cabin, sans-serif" font-weight="700" font-size="11" fill="var(--navy)">$</text><path d="M9 30h8l5 2h7a2 2 0 0 1 0 4h-8 9l8-5a2 2 0 0 1 3 3l-9 7H9z" fill="#fff"/></svg>
  </div>

  <div class="feature" style="left:29px">
    <div class="feature__title">Damage Guarantee</div>
    <p class="feature__text">Moving can be a stressful experience, and your local Austin movers can help. That is why we want to make this process as easy as possible for you and provide additional damage coverage at no extra cost.</p>
  </div>
  <div class="feature" style="left:135px">
    <div class="feature__title">On Time Guarantee</div>
    <p class="feature__text">At Hilltop Haulers, we value your time. As part of our excellent service, we guarantee that we will arrive on time for your move, or we will discount your final moving price. We believe in taking care of our customers.</p>
  </div>
  <div class="feature" style="left:241px">
    <div class="feature__title">No Hidden Fees</div>
    <p class="feature__text">After years of moving thousands of Austin families and residents, we have learned that trust is essential for a successful move. That’s why we make it our top priority to earn your trust and confidence.</p>
  </div>

  <div class="abs brand" style="left:29px;top:350px">
    <span class="brand__dot"></span>
    <span class="brand__name" style="font-size:22px">HILLTOP<br>HAULERS</span>
  </div>
  <div class="abs website" style="left:29px;top:430px">www.hilltophaulersatx.com</div>

  <div class="abs review-card">
    <div class="rating-block" style="padding-left:12px">
      <div class="rating-block__label">Customer Rating</div>
      <div class="rating-block__score">5.0 ★★★★★</div>
      <div class="rating-block__more">See all our reviews</div>
    </div>
    <p class="review-card__quote">“Very professional, took amazing care of all my furniture, moved everything pretty quick, would give more stars if possible. Thank you guys!!!</p>
    <p class="review-card__name">Marisol Ortega</p>
  </div>

  <svg class="abs" style="left:380px;top:0" width="322" height="194" viewBox="0 0 322 194">
    <rect role="img" aria-label="Photo of a family walking into their new home among moving boxes" width="322" height="194" fill="url(#photo-back)"/>
  </svg>
  <div class="service-pill" style="top:40px">RESIDENTIAL MOVING</div>
  <div class="service-pill" style="top:68px">COMMERCIAL MOVING</div>
  <div class="service-pill" style="top:95px">PACKAGING SERVICES</div>

  <div class="abs" style="left:346px;top:116px;width:90px;height:90px">
    <svg width="90" height="90"><use href="#burst"/></svg>
    <div class="abs" style="left:0;top:0;width:90px;height:90px;display:flex;align-items:center;justify-content:center;transform:rotate(-35deg);color:var(--white);font-weight:700;font-size:13.5px;line-height:14px;text-align:center;letter-spacing:1px">GET<br>A FREE<br>QUOTE</div>
  </div>

  <p class="abs tagline">Let Our Family <em>Move Yours</em></p>

  <div class="abs phone phone-bar" style="font-size:25px">
    <svg width="20" height="20" style="color:var(--white)"><use href="#phone-icon"/></svg>
    <span>512-555-0148</span>
  </div>

  <div class="address-line" style="top:314px"></div>
  <div class="address-line" style="top:352px"></div>
  <div class="address-line" style="top:390px"></div>
  <div class="address-line" style="top:428px"></div>
  <div class="abs stamp-box"></div>
</section>

</body>
</html>
```